MCP phase 1 web design

Meridale Capital Partners Ltd (MCP) is a challenger business to the traditional leasing market. We look for solutions to complex problems involving the funding of capital equipment within an office environment and then build documentation around the solution. We recently created a brief for a logo and successfully completed that assignment. We now need to create our first web site which is simply intended to be informative. To help interested designers we have attached a detailed brief that is broken into three sections. The first explains how we see the site developing over time from something quite straightforward initially to a full transaction capability. Whoever wins this competition will be expected to work with us into the future to help develop the site. Section 2 gives you a view about our likes and dislikes by reviewing some existing sites. Section 3 gives you the structure and content of the site based upon our likes and dislikes. We are by no means committed to the structure and if you believe it can be presented in a better way then please use your design. The text is fixed as content. The images to appear can be anything from photographs to line drawings again entirely at the designers whim. Currently we have a home page plus 5 subsidiary pages. A few things to help you:
1. The logo is fixed and should be amongst the downloads.
2. The colours we have are corporate and should be used.
3. The typeface we use within the business is "Verdana"
Good luck.

```html
<!DOCTYPE html>
<html lang="en">
<head>
<meta charset="utf-8">
<title>Meridale Capital Partners Ltd</title>
<link rel="stylesheet" href="https://fonts.googleapis.com/css2?family=Noto+Sans:wght@400&display=swap">
<style>
  :root {
    --page-blue: #3a86c6;
    --page-blue-dark: #2f75b3;
    --brand-blue: #2a73bc;
    --tile-blue: #4189c7;
    --tile-line: #7fb0dc;
    --nav-grey: #e6e6e6;
    --panel-grey: #ebebeb;
    --text-dark: #4a4a4a;
    --text-mid: #555555;
    --dot-active: #6cc0ea;
    --white: #ffffff;
  }
  * { margin: 0; padding: 0; box-sizing: border-box; }
  html, body {
    width: 1200px;
    height: 713px;
    overflow: hidden;
  }
  body {
    font-family: Verdana, "Noto Sans", sans-serif;
    background: linear-gradient(90deg, var(--page-blue) 0, var(--page-blue) 50px, var(--page-blue-dark) 80px, var(--page-blue-dark) 1120px, var(--page-blue) 1150px, var(--page-blue) 1200px);
    position: relative;
  }
  .page {
    position: absolute;
    left: 80px;
    top: 0;
    width: 1040px;
    height: 713px;
    background: var(--white);
  }
  .brand {
    position: absolute;
    left: 38px;
    top: 50px;
    width: 320px;
    height: 50px;
    display: flex;
    align-items: center;
    gap: 10px;
    color: var(--brand-blue);
    font-size: 19px;
    line-height: 1.2;
  }
  .brand-mark {
    width: 34px;
    height: 34px;
    background: var(--brand-blue);
    flex: none;
  }
  .main-nav {
    position: absolute;
    left: 358px;
    top: 27px;
    width: 644px;
    height: 92px;
    display: flex;
    gap: 2px;
  }
  .main-nav a {
    flex: 1;
    background: var(--nav-grey);
    color: var(--text-mid);
    text-decoration: none;
    font-size: 17px;
    display: flex;
    align-items: center;
    justify-content: center;
  }
  .brand-rule {
    position: absolute;
    left: 38px;
    top: 126px;
    width: 964px;
    height: 6px;
    background: var(--brand-blue);
  }
  .hero {
    position: absolute;
    left: 38px;
    top: 145px;
    width: 964px;
    height: 306px;
    display: flex;
  }
  .hero-image {
    position: relative;
    width: 617px;
    height: 306px;
    background: linear-gradient(90deg, #1a6878 0%, #14505f 45%, #0c2c36 75%, #0a1e26 100%);
  }
  .slider-dots {
    position: absolute;
    left: 262px;
    top: 424px;
    top: auto;
    bottom: 13px;
    display: flex;
    gap: 12px;
  }
  .slider-dots span {
    width: 14px;
    height: 14px;
    border-radius: 50%;
    background: var(--white);
  }
  .slider-dots span.is-active { background: var(--dot-active); }
  .hero-copy {
    width: 347px;
    height: 306px;
    background: var(--panel-grey);
    color: var(--text-dark);
    font-size: 16.4px;
    line-height: 20px;
    padding: 14px 18px 0 25px;
  }
  .hero-copy p + p { margin-top: 20px; }
  .solutions {
    position: absolute;
    left: 38px;
    top: 462px;
    width: 964px;
    height: 142px;
    display: flex;
    background: var(--tile-blue);
  }
  .solutions a {
    flex: 1;
    color: var(--white);
    text-decoration: none;
    font-size: 17.5px;
    display: flex;
    align-items: center;
    justify-content: center;
    padding-bottom: 4px;
  }
  .solutions a + a { border-left: 2px solid var(--tile-line); }
  .site-footer {
    position: absolute;
    left: 0;
    top: 651px;
    width: 1040px;
    text-align: center;
    color: var(--text-mid);
    font-size: 17px;
    line-height: 21px;
  }
</style>
</head>
<body>
  <div class="page">
    <header>
      <div class="brand">
        <span class="brand-mark"></span>
        <span class="brand-name">MCP Meridale Capital Partners Ltd</span>
      </div>
      <nav class="main-nav">
        <a href="#">Why Meridale</a>
        <a href="#">Solutions</a>
        <a href="#">Contacts</a>
      </nav>
      <div class="brand-rule"></div>
    </header>

    <section class="hero">
      <div class="hero-image" role="img" aria-label="Businessman in a suit holding out his open hand beneath a glowing world map with standing figures of people">
        <div class="slider-dots">
          <span class="is-active"></span><span></span><span></span><span></span>
        </div>
      </div>
      <div class="hero-copy">
        <p>We provide "<em>Sales Aid Finance</em>" through MERIDALE financial and contract solutions. Specialising in the Print and Technology markets, we offer Value Added Resellers (VARs) a range of innovative, cost effective, value added contract and finance options to enhance their sales.</p>
        <p>Our solutions are fully financed and we are totally independent from any VAR, technology provider or traditional finance house.</p>
      </div>
    </section>

    <nav class="solutions">
      <a href="#">Managed Services Solutions</a>
      <a href="#">Public Sector Solutions</a>
      <a href="#">Education Solutions</a>
    </nav>

    <footer class="site-footer">
      <p>Contacts details | adress | phones</p>
      <p>MCP 2014</p>
    </footer>
  </div>
</body>
</html>
```